Flyer für junges Unternehmen im Bereich Maschinenbau
Zielgruppe
Wir sind ein junges Unternehmen im Bereich Maschinenbau und sind spezialisiert auf Lasern von Blechen und Rohren und die gesamte Bearbeitung von Metallbaugruppen. Unsere Zielgruppe: Agrartechnik, Metallbauer, Industriekunden, Maschinenbauer - kleine sowie große Unternehmen
Aufgabenstellung
Es soll ein Flyer in DIN A5 werden, der von beiden Seiten bedruckt wird. Es soll herausstechen, was wir machen und worauf wir spezialisiert sind. Auch alle Bearbeitungsabteilung sollen erwähnt werden. Der Kunde soll auf den ersten Blick sehen, dass wir in der Metallbearbeitung dem Kunden ein Gesamtprodukt mit allen Möglichkeiten anbieten können. Der Flyer soll modern sein und Bilder im Vordergrund stehen. Auf unserer Website kann man gut erkennen, was wir alles machen.
Wenn noch andere Bilder benötigt werden, können Sie gerne auch nach Stock-Bilder recherchieren.

```html
<!DOCTYPE html>
<html lang="de">
<head>
<meta charset="utf-8">
<title>Brandt Metallform GmbH – Flyer</title>
<link rel="stylesheet" href="https://fonts.googleapis.com/css2?family=Krona+One&family=Montserrat:wght@400;500;600;700&display=swap">
<style>
  :root{
    --stage:#8c8c8c;
    --blue:#0a86c7;
    --blue-bright:#2fb3ea;
    --blue-light:#c9e9f8;
    --ink:#1b1b1b;
    --grey-frame:#d6d6d6;
    --white:#ffffff;
  }
  *{box-sizing:border-box;margin:0;padding:0}
  html,body{width:1200px;height:1117px;overflow:hidden;background:var(--stage)}
  body{position:relative;font-family:"Montserrat",sans-serif;color:var(--ink)}
  .page{position:absolute;top:194px;width:514px;height:728px;background:var(--white);overflow:hidden}
  .page--front{left:75px}
  .page--back{left:612px}
  .page svg.shapes{position:absolute;left:0;top:0}
  .abs{position:absolute}
  .brand{display:flex;align-items:center;gap:7px;color:var(--blue);font-weight:600;font-size:13px;line-height:1.15;white-space:nowrap}
  .brand__dot{width:20px;height:20px;border-radius:50%;background:var(--blue);flex:none}
  .headline{left:0;width:514px;top:360px;text-align:center;font-family:"Krona One",sans-serif;font-size:21.5px;line-height:28px;letter-spacing:-.3px}
  .headline span{display:block}
  .headline .accent{color:var(--blue)}
  .intro{left:7px;width:500px;top:430px;text-align:center;font-size:11.6px;line-height:15.5px;white-space:nowrap}
  .intro b{font-weight:700}
  .front-url{left:0;width:514px;top:684px;text-align:center;color:var(--white);font-weight:700;font-size:15px;letter-spacing:.3px}
  .about{text-align:center;font-size:10.2px;line-height:12.6px}
  .about--one{left:40px;width:434px;top:219px}
  .about--two{left:52px;width:410px;top:264px}
  .services-title{left:139px;width:234px;top:329px;height:35px;text-align:center;color:var(--white);font-weight:700;font-size:19.5px;line-height:35px}
  .service-label{width:100px;text-align:center;font-weight:700;font-size:11px;line-height:13px}
  .contact{color:var(--white);font-size:13.5px;line-height:20px;font-weight:500;white-space:nowrap}
  .contact--strong{font-weight:700}
  .contact--address{font-size:15px}
  .contact-row{display:flex;align-items:center;gap:9px}
  .contact-row svg{flex:none}
  .hours{color:var(--white);font-weight:700;font-size:11.5px;line-height:15px;white-space:nowrap}
</style>
</head>
<body>

<!-- Vorderseite -->
<section class="page page--front">
  <svg class="shapes" width="514" height="728" viewBox="0 0 514 728">
    <defs>
      <linearGradient id="bandFront" x1="0" x2="1" y1="0" y2="0">
        <stop offset="0" stop-color="#0a86c7"/><stop offset=".35" stop-color="#2fb3ea"/><stop offset="1" stop-color="#0a86c7"/>
      </linearGradient>
      <linearGradient id="photoGears" x1="0" y1="0" x2="1" y2="1">
        <stop offset="0" stop-color="#5a6fb0"/><stop offset=".5" stop-color="#8a8ea6"/><stop offset="1" stop-color="#b07b55"/>
      </linearGradient>
      <linearGradient id="photoSparks" x1="0" y1="0" x2="1" y2="1">
        <stop offset="0" stop-color="#2b2b2b"/><stop offset="1" stop-color="#6b3e22"/>
      </linearGradient>
      <polygon id="hex97" points="0,-97 84,-48.5 84,48.5 0,97 -84,48.5 -84,-48.5"/>
      <polygon id="hex88" points="0,-88 76.2,-44 76.2,44 0,88 -76.2,44 -76.2,-44"/>
      <polygon id="hex80" points="0,-80 69.3,-40 69.3,40 0,80 -69.3,40 -69.3,-40"/>
      <polygon id="hex74" points="0,-74 64.1,-37 64.1,37 0,74 -64.1,37 -64.1,-37"/>
    </defs>
    <polygon points="330,275 514,165 514,378" fill="url(#photoSparks)" role="img" aria-label="Foto: Funkenflug beim Schleifen von Metall"/>
    <polygon points="0,0 514,0 514,110 486,162 214,307 0,193" fill="url(#photoGears)" role="img" aria-label="Foto: Zahnräder und Welle einer Werkzeugmaschine"/>
    <polygon points="345,0 514,0 514,100 430,150 345,105" fill="var(--white)"/>
    <polygon points="0,300 82,262 200,330 214,340 0,345" fill="var(--blue-light)"/>
    <polygon points="0,193 214,307 486,162 486,199 214,343 0,229" fill="url(#bandFront)"/>
    <polygon points="0,693 514,585 514,728 0,728" fill="var(--blue)"/>
    <use href="#hex97" x="109" y="582" fill="var(--grey-frame)"/>
    <use href="#hex97" x="257" y="582" fill="var(--grey-frame)"/>
    <use href="#hex97" x="405" y="582" fill="var(--grey-frame)"/>
    <use href="#hex88" x="109" y="582" fill="var(--blue)"/>
    <use href="#hex88" x="257" y="582" fill="var(--blue)"/>
    <use href="#hex88" x="405" y="582" fill="var(--blue)"/>
    <use href="#hex80" x="109" y="582" fill="var(--white)"/>
    <use href="#hex80" x="257" y="582" fill="var(--white)"/>
    <use href="#hex80" x="405" y="582" fill="var(--white)"/>
    <use href="#hex74" x="109" y="582" fill="#7d7f86" role="img" aria-label="Foto: Laserkopf schneidet ein Rohr mit Funken"/>
    <use href="#hex74" x="257" y="582" fill="#b9bcc2" role="img" aria-label="Foto: lasergeschnittene Blechteile"/>
    <use href="#hex74" x="405" y="582" fill="#d9d9d9" role="img" aria-label="Foto: Fräser bearbeitet ein Werkstück"/>
  </svg>

  <div class="abs brand" style="left:358px;top:62px;">
    <span class="brand__dot"></span><span>Brandt<br>Metallform GmbH</span>
  </div>

  <h1 class="abs headline"><span>INNOVATIVE ROHR- UND</span><span class="accent">BLECHBEARBEITUNG</span></h1>
  <p class="abs intro">Brandt Metallform GmbH ist ein starker Partner im Bereich <b>Laserschneiden</b><br>von Blechen und Rohren sowie der weiteren <b>Bearbeitung ganzer</b><br><b>Baugruppen</b> mit dem Ziel kundenorientiert zu agieren.</p>
  <p class="abs front-url">www.brandt-metallform.de</p>
</section>

<!-- Rückseite -->
<section class="page page--back">
  <svg class="shapes" width="514" height="728" viewBox="0 0 514 728">
    <defs>
      <linearGradient id="bandBack" x1="0" x2="1" y1="0" y2="0">
        <stop offset="0" stop-color="#0a86c7"/><stop offset=".4" stop-color="#2fb3ea"/><stop offset="1" stop-color="#0a86c7"/>
      </linearGradient>
      <linearGradient id="photoSheet" x1="0" y1="0" x2="1" y2="1">
        <stop offset="0" stop-color="#3a3a3a"/><stop offset="1" stop-color="#1e1f22"/>
      </linearGradient>
    </defs>
    <polygon points="485,0 514,0 514,170 420,115" fill="#12161c"/>
    <polygon points="0,0 485,0 485,17 212,168 0,54" fill="url(#photoSheet)" role="img" aria-label="Foto: lasergeschnittenes Blechteil auf dem Schneidrost"/>
    <polygon points="0,144 82,159 0,205" fill="var(--blue-light)"/>
    <polygon points="0,54 212,168 485,17 485,54 212,208 0,90" fill="url(#bandBack)"/>
    <polygon points="0,648 80,604 469,604 469,378 513,352 513,728 0,728" fill="var(--blue)"/>
    <rect x="50.5" y="344.5" width="414" height="253" fill="var(--white)" stroke="var(--blue)" stroke-width="3"/>
    <polygon points="146,329 373,329 366,364 139,364" fill="var(--blue)"/>
    <circle cx="109" cy="422" r="36" fill="var(--blue)" role="img" aria-label="Symbol: Rohrbearbeitung"/>
    <circle cx="207" cy="422" r="36" fill="var(--blue)" role="img" aria-label="Symbol: Bleche"/>
    <circle cx="305" cy="422" r="36" fill="var(--blue)" role="img" aria-label="Symbol: Drehen und Fräsen"/>
    <circle cx="404" cy="422" r="36" fill="var(--blue)" role="img" aria-label="Symbol: Abkanten"/>
    <circle cx="158" cy="528" r="36" fill="var(--blue)" role="img" aria-label="Symbol: Schweißen"/>
    <circle cx="256" cy="528" r="36" fill="var(--blue)" role="img" aria-label="Symbol: Konstruktion"/>
    <circle cx="354" cy="528" r="36" fill="var(--blue)" role="img" aria-label="Symbol: Oberflächen"/>
  </svg>

  <div class="abs brand" style="left:338px;top:154px;">
    <span class="brand__dot"></span><span>Brandt<br>Metallform GmbH</span>
  </div>

  <p class="abs about about--one">Wir sind ein mittelständisches Unternehmen im Kreis Musterland mit einem modernen Maschinenpark. Von Einzelteilen bis hin zu umfassenden Baugruppen beziehen Sie unsere Produkte in kompromissloser Qualität.</p>
  <p class="abs about about--two">Durch unsere Fülle an Fertigungsprozessen und unseren Fachkenntnissen begleiten wir Ihr Produkt an einem Standort voll umfänglich von der Idee zum fertigen Produkt. Durch unseren hauseinigen Fuhrpark stellen wir eine pünktliche und mühelose Zustellung sicher.</p>

  <h2 class="abs services-title">Unsere Leistungen</h2>
  <p class="abs service-label" style="left:59px;top:463px;">Rohre</p>
  <p class="abs service-label" style="left:157px;top:463px;">Bleche</p>
  <p class="abs service-label" style="left:255px;top:463px;">Drehen und Fräsen</p>
  <p class="abs service-label" style="left:354px;top:463px;">Abkanten</p>
  <p class="abs service-label" style="left:108px;top:570px;">Schweißen</p>
  <p class="abs service-label" style="left:206px;top:570px;">Konstruktion</p>
  <p class="abs service-label" style="left:304px;top:570px;">Oberflächen</p>

  <div class="abs" style="left:72px;top:626px;">
    <div class="contact-row contact contact--strong">
      <svg width="15" height="15" viewBox="0 0 16 16"><circle cx="8" cy="8" r="8" fill="#fff"/><path d="M5.2 4.2l1.4-.3.8 1.9-.9.7c.5 1.1 1.3 1.9 2.4 2.4l.7-.9 1.9.8-.3 1.4c-3.3.1-6.1-2.7-6-6z" fill="var(--blue)"/></svg>
      <span>+49 (1234) 567890</span>
    </div>
    <div class="contact-row contact">
      <svg width="15" height="15" viewBox="0 0 16 16"><circle cx="8" cy="8" r="8" fill="#fff"/><rect x="4" y="5" width="8" height="6" fill="none" stroke="var(--blue)" stroke-width="1.2"/><path d="M4 5l4 3.2L12 5" fill="none" stroke="var(--blue)" stroke-width="1.2"/></svg>
      <span>info@brandt-metallform.de</span>
    </div>
    <div class="contact-row contact">
      <svg width="15" height="15" viewBox="0 0 16 16"><circle cx="8" cy="8" r="8" fill="#fff"/><circle cx="8" cy="8" r="4.2" fill="none" stroke="var(--blue)" stroke-width="1.1"/><path d="M3.8 8h8.4M8 3.8c-2 2.4-2 6 0 8.4M8 3.8c2 2.4 2 6 0 8.4" fill="none" stroke="var(--blue)" stroke-width="1"/></svg>
      <span>www.brandt-metallform.de</span>
    </div>
  </div>

  <div class="abs" style="left:312px;top:624px;">
    <div class="contact-row contact contact--address" style="align-items:flex-start;gap:10px;">
      <svg width="14" height="18" viewBox="0 0 14 18" style="margin-top:1px"><path d="M7 0C3.1 0 0 3 0 6.8 0 11.6 7 18 7 18s7-6.4 7-11.2C14 3 10.9 0 7 0z" fill="#fff"/><circle cx="7" cy="6.8" r="2.6" fill="var(--blue)"/></svg>
      <span>Werkstraße 12<br>12345 Musterstadt</span>
    </div>
    <p class="hours" style="margin-top:6px;">Mo. - Do. : 7:00 – 16:00 Uhr<br>Fr. : 7:00 – 12:00 Uhr</p>
  </div>
</section>

</body>
</html>
```